100% West Australian Static Banner

I require a static banner to go on a couple of pages in our website (under development) that highlights that we are a 100% Western Australian Owned & Operated company. I would prefer the banner to be in our company colours (blue shades & grey). I also would like it to be eye catching and modern in design. I have included a 100% West Australian rubber stamp logo to be used as well as including our logo so you know our colours. The banner needs to be 1139 x 350 pixels in size.

Target Market(s)

B2B

Requirements
Must have
• Our rubber stamp 100% West Australian logo
• Modern Eye Catching design
• Blue shaded background
Nice to have
• Shading background similar our logo blue colours
• 100% logo can be reversed out if required or colour changed
• Larger text saying - 100% West Australian Owned & Operated

```html
<!DOCTYPE html>
<html lang="en">
<head>
<meta charset="utf-8">
<title>100% West Australian Banner</title>
<link href="https://fonts.googleapis.com/css2?family=Bebas+Neue&family=Raleway:wght@300;600&display=swap" rel="stylesheet">
<style>
  :root {
    --night: #07142a;
    --night-edge: #0b2244;
    --globe-deep: #0f4c98;
    --globe-mid: #1d6fd0;
    --globe-light: #3f94ea;
    --land: #5aa6ee;
    --white: #ffffff;
    --flare: #bfe6ff;
    --grey: #a9b0b8;
    --brand-blue: #3a7fd6;
  }
  * { margin: 0; padding: 0; box-sizing: border-box; }
  html, body { width: 1200px; height: 370px; overflow: hidden; background: var(--night); }
  .banner {
    position: relative;
    width: 1200px;
    height: 370px;
    overflow: hidden;
    background: linear-gradient(90deg, var(--night) 0%, var(--night-edge) 50%, var(--night) 100%);
    font-family: "Bebas Neue", sans-serif;
    color: var(--white);
  }
  .backdrop { position: absolute; inset: 0; width: 1200px; height: 370px; }
  .stamp-badge { position: absolute; left: 3px; top: 40px; width: 216px; height: 216px; }
  .headline-figure {
    position: absolute;
    left: 372px;
    top: 78px;
    font-size: 198px;
    line-height: 1;
    letter-spacing: -2px;
  }
  .headline-region {
    position: absolute;
    left: 730px;
    top: 150px;
    font-size: 68px;
    line-height: 1;
    letter-spacing: 0.5px;
  }
  .headline-tagline {
    position: absolute;
    left: 734px;
    top: 216px;
    font-family: "Raleway", sans-serif;
    font-weight: 300;
    font-size: 23px;
    letter-spacing: 8.5px;
    line-height: 1;
  }
  .flare { position: absolute; left: 700px; top: 196px; width: 260px; height: 24px; }
  .brand {
    position: absolute;
    left: 888px;
    top: 283px;
    display: flex;
    align-items: center;
    gap: 10px;
  }
  .brand-square { width: 30px; height: 30px; background: var(--brand-blue); }
  .brand-name {
    font-family: "Raleway", sans-serif;
    font-weight: 600;
    font-size: 19px;
    color: var(--grey);
  }
</style>
</head>
<body>
<div class="banner">
  <svg class="backdrop" viewBox="0 0 1200 370" aria-hidden="true">
    <defs>
      <radialGradient id="globe-fill" cx="0.5" cy="0.35" r="0.7">
        <stop offset="0" stop-color="var(--globe-light)"/>
        <stop offset="0.55" stop-color="var(--globe-mid)"/>
        <stop offset="1" stop-color="var(--globe-deep)"/>
      </radialGradient>
      <radialGradient id="land-fill" cx="0.5" cy="0.5" r="0.5">
        <stop offset="0" stop-color="var(--land)" stop-opacity="0.75"/>
        <stop offset="1" stop-color="var(--land)" stop-opacity="0.15"/>
      </radialGradient>
    </defs>
    <circle class="globe" cx="630" cy="360" r="430" fill="url(#globe-fill)"/>
    <g role="img" aria-label="Satellite map of the Australian continent">
      <ellipse cx="640" cy="180" rx="300" ry="170" fill="url(#land-fill)"/>
    </g>
  </svg>

  <svg class="stamp-badge" viewBox="0 0 216 216" role="img" aria-label="Rubber stamp badge">
    <circle cx="108" cy="108" r="104" fill="var(--white)"/>
    <circle cx="108" cy="108" r="86" fill="none" stroke="var(--night)" stroke-width="5"/>
  </svg>

  <div class="headline-figure">100%</div>
  <div class="headline-region">West Austrailian</div>
  <div class="headline-tagline">OWNED &amp; OPERATED</div>

  <svg class="flare" viewBox="0 0 260 24" aria-hidden="true">
    <defs>
      <linearGradient id="flare-line" x1="0" x2="1">
        <stop offset="0" stop-color="var(--flare)" stop-opacity="0"/>
        <stop offset="0.45" stop-color="var(--white)"/>
        <stop offset="1" stop-color="var(--flare)" stop-opacity="0"/>
      </linearGradient>
      <radialGradient id="flare-glow">
        <stop offset="0" stop-color="var(--white)" stop-opacity="0.9"/>
        <stop offset="1" stop-color="var(--flare)" stop-opacity="0"/>
      </radialGradient>
    </defs>
    <ellipse cx="115" cy="12" rx="50" ry="10" fill="url(#flare-glow)"/>
    <rect x="0" y="11" width="260" height="2" fill="url(#flare-line)"/>
  </svg>

  <div class="brand">
    <span class="brand-square"></span>
    <span class="brand-name">Crestline Packaging</span>
  </div>
</div>
</body>
</html>
```